copper lantern website

We need a new website for our new business division. We are a sustainable design firm specializing in servicing the needs if architects and developers. We have a staff consisting of architects, engineers, and former contractors and we understand green must make sense.

Bottomline - the only sustainable and copper lantern solutions are those thatbare good for the environment and good for our clients bottom line.

Our company is copper lantern and we will send you a copy of our logo you will see our tagline. Is simple. sustainable. solutions. The play with the periods is that we believe their are simple sustainable solutions and we want to use the words together and possible let each stand alone to accentuate their individual meaning in regards to benefit to our clients.

We want a cool splash page with nich graphics and pictures then later pages to feature projects and design ideas.

Target Market(s)

Our target customers are architects, developers, and contractors who would need assistance with the design process for a VARN project or assisatnce with a building owner who wants to make tehir facilty more environmentally friendly and save energy costs at the same tiem.

Industry/Entity Type

Environment

Requirements
Must have
• Needs a construction look with an environmentally friendly surrounding that is pleasing to look at. Must appeal to the client not only as environmentally friendly but also a wise investment.
Nice to have
• Opportunity for a connection to Social networking including a blog.
Should not have
• A totally environmental building feel at whatever cost. We want to emphasize that it is possible to build environmental friendly and save you money over the life of your building

```html
<!DOCTYPE html>
<html lang="en">
<head>
<meta charset="utf-8">
<title>copper lantern — simple. sustainable. solutions.</title>
<link href="https://fonts.googleapis.com/css2?family=Arimo:wght@400;700&display=swap" rel="stylesheet">
<style>
  :root {
    --leaf: #4c9a2a;
    --leaf-dark: #5a8a4a;
    --nav: #7dbf45;
    --header-top: #cfe6c6;
    --header-bottom: #e9f4e4;
    --grass-light: #8fcf4a;
    --grass-dark: #2f7a1c;
    --ink: #2b2b2b;
    --body-text: #9a9a9a;
    --rule: #b5b5b5;
    --footer-band: #c8e2c0;
    --white: #ffffff;
  }
  * { margin: 0; padding: 0; box-sizing: border-box; }
  html, body { width: 1200px; height: 900px; overflow: hidden; background: var(--white); }
  body { font-family: "Arimo", Arial, sans-serif; position: relative; }

  .site-header {
    position: absolute; left: 0; top: 0; width: 1200px; height: 112px;
    background: linear-gradient(180deg, var(--header-top), var(--header-bottom));
  }
  .brand { position: absolute; left: 36px; top: 32px; display: flex; align-items: center; gap: 10px; }
  .brand-mark { width: 22px; height: 22px; background: var(--leaf); }
  .brand-name { font-size: 34px; font-weight: 400; color: var(--leaf); letter-spacing: -0.5px; line-height: 1; }
  .brand-tagline { position: absolute; left: 68px; top: 68px; font-size: 14px; color: #555; }

  .contact-block {
    position: absolute; left: 837px; top: 8px; font-size: 14px; font-weight: 700;
    color: var(--ink); line-height: 15px;
  }
  .contact-block .accent { color: var(--leaf); }
  .contact-block .email { margin-left: 18px; }

  .main-nav { position: absolute; top: 83px; left: 0; width: 1200px; }
  .main-nav a {
    position: absolute; font-size: 14.5px; font-weight: 700; color: var(--nav);
    text-decoration: none; white-space: nowrap;
  }

  .hero {
    position: absolute; left: 0; top: 112px; width: 1200px; height: 239px;
    background: linear-gradient(180deg, var(--grass-light) 0%, #5fae2e 45%, var(--grass-dark) 100%);
  }
  .hero-panel {
    position: absolute; left: 109px; top: 22px; width: 988px; height: 198px; background: var(--white);
  }
  .hero-quote {
    position: absolute; left: 18px; top: 22px; font-size: 42px; font-weight: 700;
    color: var(--leaf-dark); line-height: 50px;
  }
  .hero-house {
    position: absolute; left: 447px; top: 14px; width: 234px; height: 160px;
    background: radial-gradient(ellipse at 40% 45%, #7cc13e 0%, #4f9a26 45%, #e8ece6 72%, #ffffff 100%);
  }
  .hero-brand { position: absolute; left: 730px; top: 78px; display: flex; align-items: center; gap: 6px; }
  .hero-brand .brand-mark { width: 14px; height: 14px; }
  .hero-brand .brand-name { font-size: 24px; }

  .intro-copy {
    position: absolute; left: 108px; top: 361px; width: 722px; height: 392px; overflow: hidden;
    font-size: 13.8px; line-height: 15.7px; color: var(--body-text);
  }
  .column-rule { position: absolute; left: 892px; top: 361px; width: 1px; height: 416px; background: var(--rule); }

  .projects-title {
    position: absolute; left: 893px; width: 307px; top: 355px; text-align: center;
    font-size: 15.5px; font-weight: 700; color: var(--body-text);
  }
  .project-thumb { position: absolute; left: 942px; width: 219px; height: 130px; }
  .project-one { top: 398px; background: linear-gradient(180deg, #cfe0ee 0%, #e6e2cf 45%, #8fae6a 80%, #5f8a45 100%); }
  .project-two { top: 598px; background: linear-gradient(180deg, #9bbfd0 0%, #7e9fa8 45%, #6f9a55 75%, #3e6d2e 100%); }

  .site-footer {
    position: absolute; left: 0; top: 793px; width: 1200px; height: 107px; background: var(--footer-band);
  }
  .footer-help { position: absolute; left: 96px; top: 26px; display: flex; align-items: center; gap: 6px; }
  .footer-help .mark { font-size: 50px; font-weight: 700; color: var(--leaf); line-height: 46px; }
  .footer-help .line { font-size: 14.5px; color: var(--leaf); margin-top: 6px; }
  .copyright {
    position: absolute; left: 0; width: 1200px; top: 93px; text-align: center; font-size: 10.5px; color: var(--ink);
  }
</style>
</head>
<body>
  <header class="site-header">
    <div class="brand">
      <span class="brand-mark"></span>
      <span class="brand-name">copper lantern</span>
    </div>
    <div class="brand-tagline">simple. sustainable. solutions.</div>

    <address class="contact-block" style="font-style:normal">
      482 Birchwood Ave. Ste 210 <span class="accent">(555) 014-2288</span><br>
      Maple Falls, ON K4T 2B8 <span class="accent email">hello@copperlantern.com</span>
    </address>

    <nav class="main-nav">
      <a href="#" style="left:471px">Home</a>
      <a href="#" style="left:541px">Company</a>
      <a href="#" style="left:635px">Creative Services</a>
      <a href="#" style="left:788px">Technical Services</a>
      <a href="#" style="left:952px">Partners</a>
      <a href="#" style="left:1045px">Contact Us</a>
    </nav>
  </header>

  <section class="hero" role="img" aria-label="Close-up photograph of fresh green grass">
    <div class="hero-panel">
      <h1 class="hero-quote">“Simple<br>Sustainable<br>Solutions”</h1>
      <div class="hero-house" role="img" aria-label="Small house shape covered in grass casting a soft shadow"></div>
      <div class="hero-brand">
        <span class="brand-mark"></span>
        <span class="brand-name">copper lantern</span>
      </div>
    </div>
  </section>

  <main>
    <p class="intro-copy">Lorem ipsum dolor sit amet, consectetur adipiscing elit. Curabitur vel fringilla eros. Donec lectus ligula, iaculis eget vestibulum quis, tempus sed purus. Integer dictum mi sit amet leo condimentum iaculis. Aliquam feugiat fringilla tellus eu eleifend. Curabitur adipiscing lacinia ipsum suscipit dapibus. Morbi id urna ante, sed commodo nunc. Integer porttitor, nisi quis vehicula mollis, arcu purus ornare lacus, eu auctor nulla augue eget leo. Ut id libero magna, eu lobortis lorem. Nulla non posuere nisi. Nullam mollis lobortis nisi, sed suscipit ipsum bibendum ut. Etiam nisi est, ultrices a posuere ac, lobortis ac justo. Donec eu lectus et libero aliquam suscipit sit amet sed ipsum. Nunc eleifend suscipit ligula in commodo. Suspendisse dui dui, vulputate eu pharetra a, posuere in enim. Curabitur nec odio ligula. Nulla pulvinar placerat diam et eleifend. Lorem ipsum dolor sit amet, consectetur adipiscing elit. Curabitur vel fringilla eros. Donec lectus ligula, iaculis eget vestibulum quis, tempus sed purus. Integer dictum mi sit amet leo condimentum iaculis. Aliquam feugiat fringilla tellus eu eleifend. Curabitur adipiscing lacinia ipsum suscipit dapibus. Morbi id urna ante, sed commodo nunc. Integer porttitor, nisi quis vehicula mollis, arcu purus ornare lacus, eu auctor nulla augue eget leo. Ut id libero magna, eu lobortis lorem. Nulla non posuere nisi. Nullam mollis lobortis nisi, sed suscipit ipsum bibendum ut. Etiam nisi est, ultrices a posuere ac, lobortis ac justo. Donec eu lectus et libero aliquam suscipit sit amet sed ipsum. Nunc eleifend suscipit ligula in commodo. Suspendisse dui dui, vulputate eu pharetra a, posuere in enim. Curabitur nec odio ligula. Nulla pulvinar placerat diam et eleifend. Lorem ipsum dolor sit amet, consectetur adipiscing elit. Curabitur vel fringilla eros. Donec lectus ligula, iaculis eget vestibulum quis, tempus sed purus. Integer dictum mi sit amet leo condimentum iaculis. Aliquam feugiat fringilla tellus eu eleifend. Curabitur adipiscing lacinia ipsum suscipit dapibus. Morbi id urna ante, sed commodo nunc. Integer porttitor, nisi quis vehicula mollis, arcu purus ornare lacus, eu auctor nulla augue eget leo. Ut id libero magna, eu lobortis lorem. Nulla non posuere nisi. Nullam mollis lobortis nisi, sed suscipit ipsum bibendum ut. Etiam nisi est, ultrices a posuere ac, lobortis ac justo. Donec eu lectus et libero aliquam suscipit sit amet sed ipsum. Nunc eleifend suscipit ligula in commodo. Suspendisse dui dui, vulputate eu pharetra a, posuere in enim. Curabitur nec odio ligula. Nulla pulvinar placerat diam et eleifend. Lorem ipsum dolor sit amet, consectetur adipiscing elit.</p>

    <div class="column-rule"></div>

    <aside>
      <h2 class="projects-title">Some of our Projects</h2>
      <div class="project-thumb project-one" role="img" aria-label="Rendering of a curved multi-storey building with planted terraces"></div>
      <div class="project-thumb project-two" role="img" aria-label="Rendering of glass office towers beside a green lawn and trees"></div>
    </aside>
  </main>

  <footer class="site-footer">
    <div class="footer-help">
      <span class="mark">?</span>
      <span class="line">Questions? Contact us / email / call &nbsp;(555) 014-2288</span>
    </div>
    <p class="copyright">Copyright 2011, copperlantern All rights reserved.</p>
  </footer>
</body>
</html>
```